Commercial Real Estate Executive Recruiting Firm Needs Business Card Design

We need a business card design for MARLOW | Executive Recruiting - an executive recruiting firm focused exclusively on the commercial real estate industry. We place professionals ranging from Analyst to the Executive Office covering all investment/finance disciplines (acquisitions, asset management, capital markets, etc.) in all product types (office, retail, multifamily, industrial, land, etc.). We have a passion for helping people (clients and candidates) and have a reputation for being open and honest in our recruiting - and yes, very successful. We have recently developed a new logo and would like to update our business cards as well. I've uploaded some information about our company that contains the new logo.

Target Market(s)

Commercial Real Estate professionals. Primarily in the US. These are typically, smart, driven professionals with finance degrees and MBAs. Primarily men between the ages of 25 and 55.

Industry/Entity Type

Real Estate

Font styles to use
Other font styles liked:
• The font for "MARLOW" is Blair ITC (Medium), and "executive recruiting" is Gotham (Book).

Requirements
Must have
• I like the idea of white background on one side and solid color (blue, black, etc.) on back of card.

Would like to utilize the fonts in the logo (to the extent possible) so as to not have too many fonts on card.
Nice to have
• I think the roles (i.e., Acquisitions, Asset Management, etc.,...) is probably likely best placed on the back side of the card with the logo maybe. See attached current business card for content.

```html
<!DOCTYPE html>
<html lang="en">
<head>
<meta charset="utf-8">
<title>MARLOW Executive Recruiting — Business Card</title>
<link rel="stylesheet" href="https://fonts.googleapis.com/css2?family=Montserrat:wght@300;400;500&family=Oswald:wght@300;400;500&display=swap">
<style>
  :root{
    --page:#e9e9ea;
    --card-white:#ffffff;
    --card-black:#0b0b0c;
    --ink:#1a1a1a;
    --ink-soft:#4a4a4a;
    --rule:#9a9a9a;
    --band-grey:#6b6b6b;
    --band-black:#050505;
    --accent:#3f86c6;
    --paper-text:#f2f2f2;
  }
  *{box-sizing:border-box;margin:0;padding:0}
  html,body{width:1200px;height:1000px;overflow:hidden}
  body{background:var(--page);font-family:"Montserrat",sans-serif;color:var(--ink);position:relative}

  .card{
    position:absolute;top:350px;width:525px;height:300px;
    box-shadow:0 6px 18px rgba(0,0,0,.18);
  }
  .card--front{left:50px;background:var(--card-white)}
  .card--back{left:625px;background:var(--card-black)}

  /* front */
  .holder{
    position:absolute;top:26px;left:170px;
    font-family:"Oswald",sans-serif;font-weight:400;font-size:13px;letter-spacing:1px;color:var(--ink-soft);
  }
  .brand{position:absolute;display:flex;align-items:center;gap:10px}
  .brand__square{width:22px;height:22px;background:currentColor;flex:none}
  .brand__text{font-family:"Montserrat",sans-serif;font-weight:300;line-height:1}
  .brand__name{display:block;letter-spacing:.38em}
  .brand__tag{display:block;letter-spacing:.22em;margin-top:4px}
  .card--front .brand{top:60px;left:110px;color:var(--ink-soft)}
  .card--front .brand__name{font-size:24px}
  .card--front .brand__tag{font-size:8.5px}

  .divider{position:absolute;top:56px;left:318px;width:1px;height:56px;background:var(--rule)}
  .specialty{position:absolute;top:64px;left:332px;font-family:"Oswald",sans-serif;color:var(--ink-soft)}
  .specialty__title{font-size:15px;font-weight:400;letter-spacing:.5px}
  .specialty__sub{font-size:12px;font-weight:300;margin-top:2px}

  .phone{position:absolute;top:124px;right:28px;font-family:"Oswald",sans-serif;font-size:13px;font-weight:400;letter-spacing:1px;color:var(--ink-soft)}

  .disciplines{
    position:absolute;top:160px;left:0;width:100%;height:28px;
    background:linear-gradient(90deg,var(--band-grey) 0%,#3a3a3a 35%,var(--band-black) 55%,var(--band-black) 100%);
    display:flex;align-items:center;justify-content:center;
    font-family:"Oswald",sans-serif;font-weight:300;font-size:12.5px;letter-spacing:.6px;color:var(--paper-text);
    white-space:nowrap;
  }
  .disciplines span{margin:0 6px;color:#bdbdbd}

  .web{position:absolute;bottom:28px;left:26px;font-size:10px;color:var(--ink-soft)}
  .email{position:absolute;bottom:28px;right:28px;font-size:10px;color:var(--ink-soft)}

  /* back */
  .card--back .brand{top:50%;left:50%;transform:translate(-50%,-50%);color:var(--paper-text)}
  .card--back .brand__square{background:var(--accent)}
  .card--back .brand__name{font-size:30px}
  .card--back .brand__tag{font-size:10.5px}
</style>
</head>
<body>
  <section class="card card--front" aria-label="Business card front">
    <p class="holder">Jordan Hale | President</p>

    <div class="brand">
      <span class="brand__square"></span>
      <span class="brand__text">
        <span class="brand__name">MARLOW</span>
        <span class="brand__tag">executive recruiting</span>
      </span>
    </div>

    <span class="divider"></span>
    <div class="specialty">
      <p class="specialty__title">COMMERCIAL REAL ESTATE RECRUITING</p>
      <p class="specialty__sub">Analyst to Executive Office Placement</p>
    </div>

    <p class="phone">M | 214 555 0148</p>

    <p class="disciplines">Acquisitions<span>|</span>Asset Management<span>|</span>Banking<span>|</span>Development<span>|</span>Capital Markets<span>|</span>Brokerage</p>

    <p class="web">www.marlowrecruiting.com</p>
    <p class="email">jordan@marlowrecruiting.com</p>
  </section>

  <section class="card card--back" aria-label="Business card back">
    <div class="brand">
      <span class="brand__square"></span>
      <span class="brand__text">
        <span class="brand__name">MARLOW</span>
        <span class="brand__tag">executive recruiting</span>
      </span>
    </div>
  </section>
</body>
</html>
```